Brightwell Acupuncture Studio Website Design

We are working with Brightwell Acunpuncture Studio. They are a local Chinese medicine and acupuncture studio and in need of a new website design.

Some sites to use for inspiration:

https://marbleriveracupuncture.example
https://cedarglowacupuncture.example
https://quietharborclinic.example
https://emberfieldacupuncture.example
https://fernhollowclinic.example

Thank you for taking the time to consider designing a website for us. We are web developers based in Stockton, CA, USA. Most of our projects go through the same process. Understanding this process may help you win a project with us. We custom-code all of our websites in-house. We don’t have any requirements as to what tools you use for your design, but we prefer Figma files. For any design that we label as four-stars, we send it to the client for review. The client picks the final design they want us to use. Once we complete this process, we will continue to show additional clients all the four-star sites and purchase them later. Your designs will have multiple chances to sell. For better chances of success, we ask that you follow these guidelines.

IMAGES:
If you use any images or icons in the design, we ask that you have a link to the asset so we can purchase the image/icon. Most of the designs we submit do not have the customer’s images on them unless they have some great images. Be creative; show us the feeling you are trying to portray with your image choices. Use any royalty-free site you choose. We subscribe to Vantrel and mainly use their images, but we can purchase images outside of Vantrel.

PLEASE NOTE: we will not submit designs to clients with watermarks on the images.

FONTS:
We ask that you identify the fonts used in the design. This can be done in a message if you want. We typically use Google Fonts and Vantrel Fonts.

CONTENT:
We're always open to different content and ideas. We often submit designs with stock images so the client can see our vision. We typically take pictures after the website launch to use their images with our vision. Lorem Ipsum is fine for paragraphs, but we ask that you write the headers in correct English. We want to be able to show the vision and identify the sections of the website.

INSPIRATION:
We typically add a couple of links in the brief of websites we like to help you get started in your design.

REVISIONS:
We do not often ask for revisions of the designs unless we see something in the design that may not appeal to the client. If there are slight changes that we want to make, we do that in the development process.

FEEDBACK:
We rarely give feedback on designs during the design process. We are working on many website projects and do not have the time to provide feedback. We usually respond if your request is well thought out and asks specific questions, but a note asking “feedback, please” usually goes unanswered.

```html
<!DOCTYPE html>
<html lang="en">
<head>
<meta charset="utf-8">
<title>Brightwell Acupuncture Studio</title>
<link href="https://fonts.googleapis.com/css2?family=Marcellus&family=Montserrat:wght@400;500;600&display=swap" rel="stylesheet">
<style>
:root{
  --red:#d4504c;
  --red-dark:#b9403d;
  --navy:#1f2630;
  --nav:#252a31;
  --ink:#2b2b2b;
  --muted:#555;
  --pink:#fbe4de;
  --grey:#ececec;
  --white:#fff;
}
*{margin:0;padding:0;box-sizing:border-box}
html,body{width:1200px;height:4776px;overflow:hidden}
body{position:relative;background:var(--white);font-family:"Montserrat",sans-serif;color:var(--ink)}
.abs{position:absolute}
h1,h2,h3,.serif{font-family:"Marcellus",serif;font-weight:400}
.btn{display:inline-block;background:var(--red);color:#fff;font-size:15px;padding:14px 34px;border-radius:3px;font-weight:500}
.btn.dark{background:var(--navy)}
.photo{position:absolute;overflow:hidden}
p.body{font-size:15px;line-height:1.75;color:var(--muted)}
.red{color:var(--red)}

/* header */
.topbar{left:0;top:0;width:1200px;height:88px;background:#fff}
.brand{left:60px;top:14px;display:flex;align-items:center;gap:12px}
.brand .dot{width:46px;height:46px;border-radius:50%;background:var(--red)}
.brand .name{font-family:"Montserrat",sans-serif;font-weight:600;font-size:22px;line-height:1.1;color:var(--navy)}
.call{left:630px;top:32px;font-size:15px;font-weight:600;color:var(--red);display:flex;align-items:center;gap:10px}
.topbar .btn{position:absolute;left:880px;top:20px;font-size:13px;padding:14px 30px}
.nav{left:0;top:88px;width:1200px;height:56px;background:var(--nav)}
.nav ul{list-style:none;display:flex;gap:42px;position:absolute;left:235px;top:0;height:56px;align-items:center}
.nav li{color:#fff;font-size:15px}
.nav li.active{background:var(--red);padding:7px 16px;border-radius:3px;display:flex;gap:8px;align-items:center}

/* hero */
.hero{left:0;top:144px;width:1200px;height:700px;background:linear-gradient(100deg,#5b2e22 0%,#8d5442 35%,#c8917a 60%,#e9c9b7 100%)}
.hero-copy{left:70px;top:200px;color:#fff}
.hero-copy h1{font-size:84px;line-height:1}
.hero-copy .sub{font-family:"Marcellus",serif;font-size:46px;margin-top:4px}
.hero-copy .lead{font-family:"Montserrat",sans-serif;font-size:32px;line-height:1.25;margin-top:14px;font-weight:500}
.hero-copy .btn{margin-top:34px;font-size:14px}
.arrow{font-size:30px;color:#fff}

/* welcome */
.welcome h2{font-size:54px;line-height:1.12;color:var(--navy)}

/* services */
.services{left:0;top:1440px;width:1200px;height:820px;background:var(--pink)}
.section-title{width:1200px;text-align:center;font-size:52px;color:var(--navy)}
.card{position:absolute;top:200px;width:330px;height:520px}
.card .arch{position:absolute;left:0;top:0;width:330px;height:300px;border-radius:165px 165px 0 0}
.card .box{position:absolute;left:20px;top:260px;width:290px;height:250px;background:#fff;text-align:center;padding:26px 18px}
.card h3{font-size:26px;line-height:1.1;color:var(--red)}
.card p{font-size:13px;line-height:1.6;color:var(--muted);margin:12px 0 18px}
.card .btn{font-size:14px;padding:12px 28px}

/* meet */
.meet h2{font-size:54px;line-height:1.1;color:var(--navy)}
.checks{list-style:none}
.checks li{font-size:14px;color:var(--muted);margin-bottom:14px;display:flex;gap:12px;align-items:center}
.checks li::before{content:"";width:14px;height:14px;border-radius:50%;background:var(--red);flex:none}

/* testimonials */
.stories{left:0;top:2840px;width:1200px;height:400px;background:var(--red);color:#fff;text-align:center}
.stories h2{font-size:48px;padding-top:60px}
.stars{font-size:30px;color:#f6c244;letter-spacing:4px;margin-top:10px}
.stories .quote{font-family:"Marcellus",serif;font-size:30px;margin-top:6px}
.stories p{font-size:15px;line-height:1.7;width:900px;margin:10px auto 0}
.stories .who{margin-top:14px;font-size:16px}

/* blog */
.blog h2{font-size:52px;color:var(--navy)}
.post{position:absolute;top:3420px;width:330px}
.post .img{width:330px;height:210px}
.post h3{font-family:"Montserrat",sans-serif;font-size:22px;line-height:1.3;font-weight:500;color:var(--ink);margin-top:18px}
.post a{display:block;color:var(--red);font-size:14px;margin-top:14px;text-decoration:none}

/* cta */
.cta{left:0;top:3820px;width:1200px;height:500px;background:var(--grey)}
.cta h2{font-size:56px;color:var(--navy)}

/* footer */
.footer{left:0;top:4320px;width:1200px;height:456px;background:var(--navy);color:#fff}
.footer h4{font-size:20px;font-weight:500;margin-bottom:22px}
.footer li{list-style:none;font-size:14px;color:#cfd3d8;margin-bottom:10px;display:flex;gap:10px;align-items:flex-start}
.field{width:250px;height:40px;background:#fff;color:#888;font-size:13px;padding:11px 14px}
.social{display:flex;gap:14px;margin-top:22px}
.social span{width:22px;height:22px;border-radius:50%;border:2px solid #fff}
.copy{left:0;top:4720px;width:1200px;text-align:center;font-size:13px;color:#b8bec6;border-top:1px solid #39414d;padding-top:18px}
</style>
</head>
<body>

<!-- header -->
<header class="abs topbar">
  <div class="abs brand"><span class="dot"></span><span class="name">Brightwell<br>Acupuncture Studio</span></div>
  <div class="abs call">
    <svg width="18" height="18" viewBox="0 0 24 24"><path fill="#d4504c" d="M6.6 10.8a15.2 15.2 0 006.6 6.6l2.2-2.2c.3-.3.7-.4 1-.2 1.1.4 2.3.6 3.6.6.6 0 1 .4 1 1V20c0 .6-.4 1-1 1A17 17 0 013 4c0-.6.4-1 1-1h3.5c.6 0 1 .4 1 1 0 1.3.2 2.5.6 3.6.1.3 0 .7-.2 1z"/></svg>
    CALL: +1 555-014-2290
  </div>
  <span class="btn">BOOK AN APPOINTMENT</span>
</header>
<nav class="abs nav">
  <ul>
    <li class="active"><svg width="14" height="14" viewBox="0 0 24 24"><path fill="#fff" d="M12 3l9 8h-3v9h-5v-6h-2v6H6v-9H3z"/></svg>Home</li>
    <li>Services</li><li>About</li><li>FAQs</li><li>Reviews</li><li>Blog</li><li>Contact</li>
  </ul>
</nav>

<!-- hero -->
<section class="abs hero" role="img" aria-label="Woman relaxing on a treatment table while acupuncture needles are placed on her face"></section>
<div class="abs hero-copy">
  <h1>Brightwell</h1>
  <div class="sub">Acupuncture Studio</div>
  <div class="lead">We are a local Chinese medicine<br>and acupuncture studio.</div>
  <span class="btn">BOOK AN APPOINTMENT</span>
</div>
<svg class="abs" style="left:0;top:760px" width="1200" height="90" viewBox="0 0 1200 90"><path d="M0 50 C300 100 600 0 900 40 C1050 60 1130 40 1200 30 L1200 90 L0 90Z" fill="#fff"/></svg>
<div class="abs arrow" style="left:70px;top:786px">&#8249;</div>
<div class="abs arrow" style="left:100px;top:786px">&#8250;</div>

<!-- welcome -->
<section class="welcome">
  <div class="photo" style="left:70px;top:880px;width:330px;height:380px;border-radius:165px 165px 0 0;background:linear-gradient(160deg,#8aa56b,#c9a27b 60%,#7a5236)" role="img" aria-label="Bowl of acupuncture needles with herbs and leaves"></div>
  <div class="photo" style="left:240px;top:1110px;width:230px;height:200px;border:6px solid #fff;background:linear-gradient(135deg,#d8b4a0,#a8705a)" role="img" aria-label="Practitioner placing needles on a patient's back"></div>
  <h2 class="abs" style="left:540px;top:930px">Welcome to <span class="red">Brightwell</span><br>Acupuncture Studio</h2>
  <p class="abs body" style="left:540px;top:1080px;width:560px">Nemo enim ipsam voluptatem quia voluptas sit aspernatur aut odit aut fugit, sed quia consequuntur magni dolores eos qui ratione voluptatem sequi nesciunt. Neque porro quisquam est, qui dolorem ipsum quia dolor sit amet, consectetur, adipisci velit, sed quia non numquam eius modi tempora incidunt ut labore et dolore magnam aliquam quaerat voluptatem.</p>
  <span class="abs btn" style="left:540px;top:1270px">Read More</span>
</section>

<!-- services -->
<section class="abs services">
  <svg class="abs" style="left:0;top:-40px" width="1200" height="60" viewBox="0 0 1200 60"><path d="M0 40 C300 0 700 60 1200 20 L1200 60 L0 60Z" fill="#fbe4de"/></svg>
  <h2 class="abs section-title" style="top:100px">Our Services</h2>
  <div class="card" style="left:75px">
    <div class="arch photo" style="background:linear-gradient(160deg,#e6c3b0,#b07d66)" role="img" aria-label="Acupuncture needles along a patient's back"></div>
    <div class="box"><h3>Whole-Body<br>Acupuncture</h3><p>Sed ut perspiciatis unde omnis iste natus error sit voluptatem accusantium doloremque laudantium.</p><span class="btn dark">Read More</span></div>
  </div>
  <div class="card" style="left:435px">
    <div class="arch photo" style="background:linear-gradient(160deg,#f0d2c2,#c0907a)" role="img" aria-label="Cosmetic acupuncture needles on a woman's forehead"></div>
    <div class="box"><h3>Cosmetic<br>Acupuncture</h3><p>Sed ut perspiciatis unde omnis iste natus error sit voluptatem accusantium doloremque laudantium.</p><span class="btn">Read More</span></div>
  </div>
  <div class="card" style="left:795px">
    <div class="arch photo" style="background:linear-gradient(160deg,#eed6c8,#b98a74)" role="img" aria-label="Microneedling treatment on a relaxed patient's face"></div>
    <div class="box"><h3>Microneedling<br>Acupuncture</h3><p>Sed ut perspiciatis unde omnis iste natus error sit voluptatem accusantium doloremque laudantium.</p><span class="btn dark">Read More</span></div>
  </div>
</section>

<!-- meet -->
<section class="meet">
  <h2 class="abs" style="left:70px;top:2180px">Meet Our<br><span class="red">Acupuncturist</span></h2>
  <p class="abs body" style="left:70px;top:2310px;width:680px">Nemo enim ipsam voluptatem quia voluptas sit aspernatur aut odit aut fugit, sed quia consequuntur magni dolores eos qui ratione voluptatem sequi nesciunt. Neque porro quisquam est, qui dolorem ipsum quia dolor sit amet, consectetur, adipisci velit, sed quia non numquam eius modi tempora incidunt ut labore et dolore magnam aliquam quaerat voluptatem.</p>
  <ul class="abs checks" style="left:70px;top:2470px;width:680px">
    <li>Doctor of Acupuncture and Chinese Medicine (certified hard work)</li>
    <li>Licensed Acupuncturist (but not a woo-woo healer)</li>
    <li>Fertility Specialist (board-certified in acupuncture for natural conception as well as IVF)</li>
    <li>Functional Medicine Practitioner (yep—I'll make sense of your labs)</li>
    <li>Partner in Your Health (it's all about finding what's best for you)</li>
  </ul>
  <span class="abs btn" style="left:70px;top:2700px">Read More</span>
  <div class="photo" style="left:800px;top:2280px;width:320px;height:420px;border-radius:160px 160px 0 0;background:linear-gradient(160deg,#d9dfe2,#a99888 70%,#7e6352)" role="img" aria-label="Portrait of the studio's acupuncturist in a white coat"></div>
</section>

<!-- testimonials -->
<section class="abs stories">
  <svg class="abs" style="left:0;top:-30px" width="1200" height="40" viewBox="0 0 1200 40"><path d="M0 30 C400 0 800 40 1200 10 L1200 40 L0 40Z" fill="#d4504c"/></svg>
  <h2>Patient Success Stories</h2>
  <div class="stars">&#9733;&#9733;&#9733;&#9733;&#9733;</div>
  <div class="quote">Quis autem vel eum iure reprehenderit qui in ea voluptate</div>
  <p>Nemo enim ipsam voluptatem quia voluptas sit aspernatur aut odit aut fugit, sed quia consequuntur magni dolores eos qui ratione voluptatem sequi nesciunt. Neque porro quisquam est, qui dolorem ipsum quia dolor sit amet, consectetur, adipisci velit, sed quia non numquam eius modi tempora incidunt ut labore et dolore magnam aliquam quaerat voluptatem.</p>
  <div class="who">- Name Heading</div>
  <div class="abs arrow" style="left:50px;top:180px;font-size:44px">&#8249;</div>
  <div class="abs arrow" style="left:1130px;top:180px;font-size:44px">&#8250;</div>
  <svg class="abs" style="left:0;top:390px" width="1200" height="40" viewBox="0 0 1200 40"><path d="M0 0 L1200 0 L1200 20 C800 40 400 0 0 30Z" fill="#d4504c"/></svg>
</section>

<!-- blog -->
<section class="blog">
  <h2 class="abs" style="left:70px;top:3290px">Blog Posts</h2>
  <div class="abs" style="left:1060px;top:3290px;font-size:34px;color:var(--navy)">&#8249;&nbsp;&nbsp;&#8250;</div>
  <div class="post" style="left:70px"><div class="img photo" style="position:relative;background:linear-gradient(135deg,#c99680,#7b4a38)" role="img" aria-label="Therapist treating a patient's back"></div><h3>Nemo enim ipsam voluptat em quia voluptas sit asperna tur aut...</h3><a>Read More</a></div>
  <div class="post" style="left:435px"><div class="img photo" style="position:relative;background:linear-gradient(135deg,#6b4a3c,#d3aa92)" role="img" aria-label="Ear acupuncture needles close-up"></div><h3>Nemo enim ipsam voluptat em quia voluptas sit asperna tur aut...</h3><a>Read More</a></div>
  <div class="post" style="left:800px"><div class="img photo" style="position:relative;background:linear-gradient(135deg,#e0c29a,#a57a4d)" role="img" aria-label="Acupuncture model showing meridian points"></div><h3>Nemo enim ipsam voluptat em quia voluptas sit asperna tur aut...</h3><a>Read More</a></div>
</section>

<!-- cta -->
<section class="abs cta">
  <div class="photo" style="left:130px;top:40px;width:340px;height:400px;border-radius:170px 170px 0 0;background:linear-gradient(170deg,#7a9a5c,#a69a92 50%,#6d6670)" role="img" aria-label="Smooth stone with acupuncture needles and a green plant"></div>
  <h2 class="abs" style="left:510px;top:140px">Ready to <span class="red">Feel Better?</span></h2>
  <p class="abs body" style="left:510px;top:230px;width:620px">Nemo enim ipsam voluptatem quia voluptas sit aspernatur aut odit aut fugit, sed quia consequuntur magni dolores eos qui ratione voluptatem sequi nesciunt. Neque porro quisquam est, qui dolorem ipsum quia dolor sit amet, consectetur, adipisci velit, sed quia non numquam eius modi tempora incidunt ut labore et dolore magnam aliquam quaerat voluptatem.</p>
  <span class="abs btn" style="left:510px;top:380px">Book an Appointment</span>
</section>

<!-- footer -->
<footer class="abs footer">
  <div class="abs brand" style="left:70px;top:120px"><span class="dot"></span><span class="name" style="color:#fff;font-size:24px">Brightwell<br>Acupuncture Studio</span></div>
  <div class="abs" style="left:370px;top:70px">
    <h4>Services</h4>
    <ul><li>Nemo enim ipsam</li><li>Voluptatem quia</li><li>Voluptas sit aspernatur</li><li>Autconsectetur</li></ul>
  </div>
  <div class="abs" style="left:610px;top:70px">
    <h4>Contact</h4>
    <ul>
      <li><svg width="14" height="16" viewBox="0 0 24 24"><path fill="#fff" d="M12 2a7 7 0 00-7 7c0 5 7 13 7 13s7-8 7-13a7 7 0 00-7-7zm0 9.5A2.5 2.5 0 1112 6a2.5 2.5 0 010 5.5z"/></svg>48 Linden Row Suite 12,<br>Stockton CA 95202, United States</li>
      <li><svg width="14" height="14" viewBox="0 0 24 24"><path fill="#fff" d="M6.6 10.8a15.2 15.2 0 006.6 6.6l2.2-2.2c.3-.3.7-.4 1-.2 1.1.4 2.3.6 3.6.6.6 0 1 .4 1 1V20c0 .6-.4 1-1 1A17 17 0 013 4c0-.6.4-1 1-1h3.5c.6 0 1 .4 1 1 0 1.3.2 2.5.6 3.6.1.3 0 .7-.2 1z"/></svg>+1 555-014-2290</li>
      <li><svg width="14" height="14" viewBox="0 0 24 24"><path fill="#fff" d="M3 5h18v14H3zm2 2v.5l7 4.5 7-4.5V7z"/></svg>hello@brightwellstudio.example</li>
    </ul>
  </div>
  <div class="abs" style="left:880px;top:70px">
    <h4>Email Subscribe</h4>
    <div class="field">Enter Email</div>
    <span class="btn" style="display:block;width:250px;text-align:center;margin-top:14px;padding:11px 0">Subscribe</span>
    <div class="social"><span></span><span></span><span></span><span></span><span></span></div>
  </div>
</footer>
<div class="abs copy">Copyright &copy; 2025 Brightwell Studio. All Right Reserved</div>

</body>
</html>
```